Packaging designed for both the bar and the box for retail and online sales

The name of the product is Plume Crumb. We manufacture a consumer package good product that's a healthy edible cookie dough bar. The product look, feels and tastes like cookie dough. It's sold in the refrigerator section of retail stores next to cookie dough and tundra loaf. The product is Gluten Free, Diary Free and include B-12, Biotin and Collagen. The ingredients are natural. When design this think about who eat cookie dough and how to engage the buyer in purchasing the product.

We needs design packaging designed for both the bar and the box. I have attached the die lines for both products.

Target Market(s)

Our customer is 16-45. Primarily female but really anyone. Middle to upper income. Interest include healthy life style and yoga. Like to eat something sweet but not feel guilty.

Colors

Designer to choose colors to be used in the design.

Requirements
Must have
• Must be clean, warm, inviting. Brand designs I really like are Tundra Loaf.
Should not have
• Should not have a photo of food

```html
<!DOCTYPE html>
<html lang="en">
<head>
<meta charset="utf-8">
<title>Plume Crumb Cookie Dough Bar – Wrapper</title>
<link href="https://fonts.googleapis.com/css2?family=Anton&family=Oswald:wght@300;400;600&display=swap" rel="stylesheet">
<style>
  :root {
    --paper: #ffffff;
    --cream: #efe6d6;
    --cream-shade: #e3d8c4;
    --cocoa: #3f2a1f;
    --cocoa-deep: #33221a;
    --amber: #e59a2e;
    --tan: #d99a4c;
  }
  html, body {
    margin: 0;
    width: 1200px;
    height: 669px;
    overflow: hidden;
    background: var(--paper);
  }
  .wrapper-art { display: block; width: 1200px; height: 669px; }
  .brand-name { font-family: "Oswald", sans-serif; font-weight: 600; fill: var(--tan); }
  .product-line { font-family: "Oswald", sans-serif; font-weight: 400; fill: var(--cocoa); }
  .product-type { font-family: "Anton", sans-serif; fill: var(--cocoa); }
  .claim { font-family: "Oswald", sans-serif; font-weight: 300; fill: var(--cocoa); letter-spacing: 5px; }
  .flavour { font-family: "Oswald", sans-serif; font-weight: 600; fill: var(--cocoa); }
  .net-weight { font-family: "Oswald", sans-serif; font-weight: 300; fill: var(--cream); letter-spacing: 1px; }
</style>
</head>
<body>
<svg class="wrapper-art" viewBox="0 0 1200 669" xmlns="http://www.w3.org/2000/svg">
  <defs>
    <linearGradient id="cream-to-cocoa" x1="0" x2="1" y1="0" y2="0">
      <stop offset="0" stop-color="var(--cream)"/>
      <stop offset="0.5" stop-color="var(--cream)"/>
      <stop offset="0.62" stop-color="var(--cocoa)"/>
      <stop offset="1" stop-color="var(--cocoa)"/>
    </linearGradient>
  </defs>

  <!-- seal ends -->
  <rect class="seal seal-left" x="170" y="192" width="130" height="256" fill="var(--cream-shade)"/>
  <rect class="seal seal-right" x="900" y="180" width="120" height="280" fill="var(--cocoa-deep)"/>

  <!-- wrapper body -->
  <rect class="wrapper-body" x="290" y="205" width="620" height="235" fill="var(--cream)"/>
  <rect class="wrapper-texture" x="560" y="205" width="350" height="235" fill="url(#cream-to-cocoa)"
        role="img" aria-label="Distressed brush texture blending cream into dark cocoa brown"/>

  <!-- brand -->
  <text class="brand-name" font-size="30" text-anchor="middle" transform="translate(318 262) rotate(-90)">PLUME CRUMB</text>

  <!-- product name -->
  <text class="product-line" font-size="46" text-anchor="middle" transform="translate(400 266) rotate(-90)">COOKIE</text>
  <text class="product-line" font-size="46" text-anchor="middle" transform="translate(444 266) rotate(-90)">DOUGH</text>
  <text class="product-type" font-size="96" text-anchor="middle" transform="translate(552 268) rotate(-90)">BAR</text>
  <text class="claim" font-size="17" text-anchor="middle" transform="translate(584 296) rotate(-90)">NATURAL</text>

  <!-- flavour badge -->
  <g class="flavour-badge">
    <circle cx="805" cy="322" r="64" fill="none" stroke="var(--amber)" stroke-width="3" stroke-dasharray="3 7"/>
    <circle cx="805" cy="322" r="52" fill="var(--cream)" stroke="var(--amber)" stroke-width="4"/>
    <circle cx="805" cy="322" r="45" fill="none" stroke="var(--amber)" stroke-width="1.5"/>
    <text class="flavour" font-size="22" text-anchor="middle" transform="translate(806 322) rotate(-90)">MAPLE</text>
    <text class="flavour" font-size="22" text-anchor="middle" transform="translate(830 322) rotate(-90)">ALMOND</text>
  </g>

  <!-- net weight -->
  <text class="net-weight" font-size="26" text-anchor="middle" transform="translate(946 322) rotate(-90)">3 OZ / 88 G</text>
</svg>
</body>
</html>
```